Website for SEO Agency That Serves Family Law Attorneys

I need a design for a website that is clean, conversion focused and professional. The site should have a parallax feel and look very up-to-date. This homepage looks a lot like what I will need https://trelvaro.com/. I will also need a professional logo that is recognizable and tells users a little about how we do SEO just by looking at it.

```html
<!DOCTYPE html>
<html lang="en">
<head>
<meta charset="utf-8">
<title>Vantolia – SEO for Family Law Attorneys</title>
<link href="https://fonts.googleapis.com/css2?family=Roboto:ital,wght@0,400;0,500;0,700;0,900;1,400&family=Roboto+Condensed:wght@700&family=Ubuntu:wght@700&family=Montserrat:wght@400;500&display=swap" rel="stylesheet">
<style>
:root{
  --navy:#14233a;
  --ink:#222;
  --text:#444;
  --red:#e03a16;
  --blue:#1b6fb5;
  --submit:#2a8fc6;
  --grey-bg:#ebebeb;
  --line:#dcdcdc;
  --white:#fff;
}
*{margin:0;padding:0;box-sizing:border-box}
html,body{width:1200px;height:4258px;overflow:hidden}
body{position:relative;font-family:'Roboto',sans-serif;color:var(--text);background:var(--white)}
.abs{position:absolute}
section,header,footer{position:absolute;left:0;width:1200px}

/* header */
.site-header{top:0;height:86px;background:var(--white)}
.brand{left:144px;top:18px;font-family:'Ubuntu',sans-serif;font-weight:700;font-size:40px;color:var(--ink);letter-spacing:1px}
.main-nav a{position:absolute;top:36px;font-size:15px;font-weight:500;color:var(--ink);text-decoration:none}

/* hero */
.hero{top:86px;height:610px;overflow:hidden}
.hero-bg{position:absolute;inset:0;background:linear-gradient(110deg,#101c2e 0%,#1b3350 50%,#2a4058 78%,#6b5a3a 100%)}
.hero h1{position:absolute;left:144px;top:140px;font-family:'Roboto Condensed',sans-serif;font-weight:700;font-size:50px;line-height:58px;color:var(--white)}
.hero p{position:absolute;left:144px;top:258px;font-size:15.5px;line-height:24px;color:var(--white)}
.signup{position:absolute;left:144px;top:322px;width:350px;height:42px;background:var(--white);border:2px solid #ddd}
.signup span{position:absolute;left:16px;top:12px;font-size:11px;color:#555}
.signup b{position:absolute;right:3px;top:3px;width:92px;height:32px;background:var(--red);color:var(--white);font-size:13px;font-weight:700;text-align:center;line-height:32px}
.dots{position:absolute;left:144px;top:396px}
.dots i{display:inline-block;width:18px;height:18px;border-radius:50%;border:2px solid var(--white);margin-right:7px}
.dots i:first-child{background:var(--white)}
.hero-wave{position:absolute;left:0;bottom:0}

/* partners */
.partners{top:696px;height:130px;border-bottom:1px solid #e4e4e4}
.partners span{position:absolute;top:48px;transform:translateX(-50%);font-size:27px;font-weight:700;color:#333;white-space:nowrap}

/* about */
.about{top:826px;height:617px}
.about-frame{left:298px;top:86px;width:756px;height:432px;border:2px solid var(--blue)}
.about-image{left:144px;top:123px;width:408px;height:350px;background:linear-gradient(180deg,#3a3a3a 0%,#55626c 45%,#8fa9c0 55%,#3c3c3c 100%)}
.about h2{left:598px;top:134px;font-size:38px;font-weight:400;color:var(--ink);letter-spacing:.5px}
.about h2 strong{font-weight:700}
.about p{left:598px;top:196px;width:425px;font-size:14px;line-height:32px;color:#333}
.btn-red{background:var(--red);color:var(--white);font-size:14.5px;font-weight:500;text-align:center}
.about .btn-red{left:598px;top:417px;width:141px;height:40px;line-height:40px}

/* cta band */
.cta{top:1443px;height:499px;overflow:hidden}
.cta-bg{position:absolute;inset:0;background:linear-gradient(100deg,#1a5fa6 0%,#2f82cc 50%,#2a7ac4 75%,#5fa6e0 100%)}
.cta h2{left:0;width:1200px;top:112px;text-align:center;font-family:'Roboto Condensed',sans-serif;font-size:36px;color:var(--white)}
.cta p{left:228px;width:744px;top:176px;text-align:center;font-size:14.5px;line-height:32.5px;color:#e6f0fa}
.cta .btn-red{left:393px;top:299px;width:197px;height:43px;line-height:43px;border-radius:22px;font-size:16px;font-weight:700}
.btn-outline{left:610px;top:299px;width:195px;height:43px;border:2px solid var(--white);border-radius:22px;color:var(--white);font-size:16px;font-weight:500;line-height:39px;padding-left:18px}
.btn-outline svg{position:absolute;right:12px;top:6px}

/* services */
.services{top:1942px;height:937px}
.section-title{left:0;width:1200px;text-align:center;font-family:'Roboto Condensed',sans-serif;font-size:38px;color:var(--ink)}
.title-rule{left:560px;width:80px;height:3px;background:var(--blue)}
.services .section-title{top:76px}
.services .title-rule{top:151px}
.vline{width:1px;background:var(--line);top:207px;height:542px}
.hline{left:142px;top:480px;width:913px;height:1px;background:var(--line)}
.service{width:262px;transform:translateX(-50%);text-align:center}
.service svg{display:block;margin:0 auto}
.service h3{font-size:19px;font-weight:500;color:var(--ink);margin-top:20px}
.service p{font-size:13px;line-height:24px;color:#555;margin-top:14px}
.btn-more{left:488px;top:802px;width:223px;height:46px;border:2px solid var(--blue);border-radius:23px;color:var(--blue);font-size:18px;text-align:center;line-height:42px}

/* reviews */
.reviews{top:2879px;height:548px;background:var(--grey-bg)}
.reviews .section-title{top:78px}
.reviews .title-rule{top:141px}
.review-card{width:400px;height:256px;top:204px}
.review-card svg.frame{position:absolute;left:0;top:0}
.avatar{width:120px;height:120px;border-radius:50%;background:radial-gradient(circle at 50% 40%,#c9d3dc,#5a6b7a);box-shadow:0 2px 6px rgba(0,0,0,.25)}
.review-text{width:276px;font-size:13px;line-height:24px;color:#333}
.reviewer{font-size:15px;font-style:italic;color:var(--ink)}
.stars{color:var(--blue);font-size:15px;letter-spacing:2px}
.quote{font-family:Georgia,serif;font-size:120px;line-height:1;color:#d6d6d6}

/* demo */
.demo{top:3427px;height:586px;overflow:hidden}
.demo-bg{position:absolute;inset:0;background:linear-gradient(180deg,#e9552c 0%,#e85a33 60%,#d9502c 100%)}
.demo h2{top:78px;left:0;width:1200px;text-align:center;font-family:'Roboto Condensed',sans-serif;font-size:38px;color:var(--white)}
.field{background:var(--white);font-size:11px;color:#333;padding:12px 16px;border:1px solid #f0c8bb}
.submit{left:507px;top:444px;width:166px;height:42px;background:var(--submit);color:var(--white);font-size:16px;font-weight:700;text-align:center;line-height:42px}

/* footer */
.site-footer{top:4013px;height:245px;font-family:'Montserrat',sans-serif;color:#222;text-align:center}
.footer-links{top:55px;left:0;width:1200px;font-size:17px}
.copyright{top:103px;left:0;width:1200px;font-size:17px}
.social{width:36px;height:36px;border-radius:50%;border:1.5px solid #333;top:155px}
</style>
</head>
<body>

<header class="site-header">
  <div class="abs brand">Vantolia</div>
  <nav class="main-nav">
    <a style="left:527px">HOME</a>
    <a style="left:613px">ABOUT US</a>
    <a style="left:729px">OUR SERVICES</a>
    <a style="left:876px">TEAM</a>
    <a style="left:960px">CONTACT US</a>
  </nav>
</header>

<section class="hero">
  <div class="hero-bg" role="img" aria-label="Dark photo backdrop with hands typing on a laptop at a round white table beside an orange chair"></div>
  <h1>FREE EXCLUSIVE<br>TRAFFIC TIPS</h1>
  <p>Enter your email below to get access to my proven<br>SEO and traffic tips</p>
  <div class="signup"><span>Email Address</span><b>SIGN UP</b></div>
  <div class="dots"><i></i><i></i><i></i></div>
  <svg class="hero-wave" width="1200" height="110" viewBox="0 0 1200 110" aria-hidden="true">
    <path d="M0 70 C120 30 260 40 420 60 C620 85 800 60 950 45 C1060 35 1140 45 1200 60 L1200 110 L0 110 Z" fill="#e7e7e9"/>
    <path d="M0 95 C160 55 330 60 520 80 C720 100 900 70 1060 62 C1120 60 1170 64 1200 68 L1200 110 L0 110 Z" fill="#fff"/>
  </svg>
</section>

<section class="partners">
  <span style="left:220px">Norvane</span>
  <span style="left:408px">Calvex</span>
  <span style="left:598px">Brightmoor</span>
  <span style="left:790px">Lindqvale</span>
  <span style="left:980px">Ostrel</span>
</section>

<section class="about">
  <div class="abs about-frame"></div>
  <div class="abs about-image" role="img" aria-label="Man standing before a chalkboard wall of SEO words with a glowing upward arrow"></div>
  <h2 class="abs"><strong>ABOUT</strong> VANTOLIA</h2>
  <p class="abs">Sed ut perspiciatis unde omnis iste natus error sit voluptatem accusantium doloremque laudantium, totam rem aperiam, eaque ipsa quae ab illo inventore veritatis et quasi architecto beatae vitae dicta sunt explicabo. Nemo enim ipsam voluptatem quia voluptas sit aspernatur aut odit aut fugi laudantium, totam rem aperiam, eaque ipsa quae ab illo inventore</p>
  <div class="abs btn-red">READ MORE</div>
</section>

<section class="cta">
  <div class="cta-bg" role="img" aria-label="Blue tinted photo of hands on a laptop with chart overlay"></div>
  <h2 class="abs">WE SERVE FAMILY LAW ATTORNEYS</h2>
  <p class="abs">Sed ut perspiciatis unde omnis iste natus error sit voluptatem accusantium doloremque laudantium, totam rem aperiam, eaque ipsa quae ab illo inventore veritatis et quasi architecto beatae vitae dicta sunt explicabo. Nemo enim ipsam voluptatem quia voluptas sit asnatur aut odit aut fugi lda totam</p>
  <div class="abs btn-red">GET MORE INFO</div>
  <div class="abs btn-outline">WATCH VIDEO
    <svg width="28" height="28" viewBox="0 0 28 28" aria-hidden="true"><circle cx="14" cy="14" r="12" fill="none" stroke="#fff" stroke-width="2"/><path d="M11 8.5 L19 14 L11 19.5 Z" fill="#fff"/></svg>
  </div>
</section>

<section class="services">
  <h2 class="abs section-title">OUR SERVICES</h2>
  <div class="abs title-rule"></div>
  <div class="abs vline" style="left:436px"></div>
  <div class="abs vline" style="left:769px"></div>
  <div class="abs hline"></div>

  <div class="abs service" style="left:271px;top:212px">
    <svg width="70" height="70" viewBox="0 0 70 70" fill="none" stroke="#1ea3c6" stroke-width="2.5"><rect x="5" y="6" width="60" height="40"/><path d="M12 38 L25 24 L35 32 L55 14"/><path d="M35 46 V56 M35 56 L22 66 M35 56 L48 66 M5 50 H65"/></svg>
    <h3>Nemo enim ipsam</h3>
    <p>Sed ut perspiciatis unde omnis iste natus error sit voluptatem accusantium dolorque laudantium, totam rem aperiam Sed ut piatis unde omnis iste natus sit</p>
  </div>
  <div class="abs service" style="left:598px;top:212px">
    <svg width="70" height="70" viewBox="0 0 70 70" fill="none" stroke="#2a86c8" stroke-width="2.5"><rect x="4" y="3" width="62" height="64"/><path d="M4 14 H66"/><circle cx="11" cy="8.5" r="2"/><circle cx="18" cy="8.5" r="2"/><circle cx="25" cy="8.5" r="2"/><path d="M12 24 H40 M12 32 H32 M12 40 H28 M12 48 H24"/><path d="M58 22 L62 26 L38 52 L32 54 L34 48 Z"/></svg>
    <h3>Nemo enim ipsam</h3>
    <p>Sed ut perspiciatis unde omnis iste natus error sit voluptatem accusantium dolorque laudantium, totam rem aperiam Sed ut piatis unde omnis iste natus sit</p>
  </div>
  <div class="abs service" style="left:927px;top:212px">
    <svg width="74" height="70" viewBox="0 0 74 70" fill="none" stroke="#1ea3c6" stroke-width="2.5"><circle cx="28" cy="28" r="22"/><circle cx="28" cy="28" r="14"/><path d="M44 44 L62 64"/><path d="M16 34 L24 24 L31 30 L40 18"/><circle cx="62" cy="8" r="4"/><path d="M50 8 H58"/></svg>
    <h3>Nemo enim ipsam</h3>
    <p>Sed ut perspiciatis unde omnis iste natus error sit voluptatem accusantium dolorque laudantium, totam rem aperiam Sed ut piatis unde omnis iste natus sit</p>
  </div>

  <div class="abs service" style="left:271px;top:508px">
    <svg width="76" height="78" viewBox="0 0 76 78" fill="none" stroke="#1ea3c6" stroke-width="2.5"><rect x="12" y="4" width="52" height="56"/><path d="M12 14 H64"/><path d="M30 24 L24 30 L30 36 M46 24 L52 30 L46 36 M40 22 L36 38"/><path d="M22 46 H54 M22 52 H44"/><path d="M4 62 H72 L68 72 H8 Z"/></svg>
    <h3>Nemo enim ipsam</h3>
    <p>Sed ut perspiciatis unde omnis iste natus error sit voluptatem accusantium dolorque laudantium, totam rem aperiam Sed ut piatis unde omnis iste natus sit</p>
  </div>
  <div class="abs service" style="left:598px;top:508px">
    <svg width="78" height="78" viewBox="0 0 78 78" fill="none" stroke="#2a86c8" stroke-width="2.5"><path d="M6 36 L39 14 L72 36 V76 H6 Z"/><path d="M6 36 L39 58 L72 36 M6 76 L32 54 M72 76 L46 54"/><rect x="22" y="24" width="34" height="22"/><path d="M28 32 H50 M28 38 H44"/><path d="M39 2 V8 M20 6 L24 12 M58 6 L54 12 M6 18 L12 20 M72 18 L66 20"/></svg>
    <h3>Nemo enim ipsam</h3>
    <p>Sed ut perspiciatis unde omnis iste natus error sit voluptatem accusantium dolorque laudantium, totam rem aperiam Sed ut piatis unde omnis iste natus sit</p>
  </div>
  <div class="abs service" style="left:927px;top:508px">
    <svg width="82" height="78" viewBox="0 0 82 78" fill="none" stroke="#1ea3c6" stroke-width="2.5"><circle cx="41" cy="10" r="7"/><path d="M29 30 Q41 16 53 30 Z"/><circle cx="14" cy="46" r="7"/><path d="M2 74 V66 Q14 52 26 66 V74 Z"/><circle cx="68" cy="46" r="7"/><path d="M56 74 V66 Q68 52 80 66 V74 Z"/><path d="M22 30 Q12 34 12 38 M60 30 Q70 34 70 38 M30 66 H50 M44 62 L50 66 L44 70"/></svg>
    <h3>Nemo enim ipsam</h3>
    <p>Sed ut perspiciatis unde omnis iste natus error sit voluptatem accusantium dolorque laudantium, totam rem aperiam Sed ut piatis unde omnis iste natus sit</p>
  </div>

  <div class="abs btn-more">View More Services</div>
</section>

<section class="reviews">
  <h2 class="abs section-title">CUSTOMERS REVIEWS</h2>
  <div class="abs title-rule"></div>

  <div class="abs review-card" style="left:183px">
    <svg class="frame" width="400" height="256" viewBox="0 0 400 256" aria-hidden="true"><path d="M16 1 H399 L385 255 H1 Z" fill="#fff" stroke="#1b6fb5" stroke-width="2"/></svg>
    <div class="abs avatar" style="left:-50px;top:59px" role="img" aria-label="Customer portrait"></div>
    <div class="abs review-text" style="left:95px;top:28px">Sed ut perspiciatis unde omnis iste natus error sit voluptatem accusantium oremque laudantium, totam rem aperiam, eaque ipsa quae ab illo inventore veritatis et quasi architecto beatae vitae dicta sunt explicabo. Nemo enim ipsam voluptatem</div>
    <div class="abs reviewer" style="left:95px;top:184px">John Doe - &nbsp;Vantolia</div>
    <div class="abs stars" style="left:95px;top:214px">★★★★★</div>
    <div class="abs quote" style="left:298px;top:170px">”</div>
  </div>

  <div class="abs review-card" style="left:656px">
    <svg class="frame" width="400" height="256" viewBox="0 0 400 256" aria-hidden="true"><path d="M16 1 H399 L385 255 H1 Z" fill="#fff" stroke="#1b6fb5" stroke-width="2"/></svg>
    <div class="abs avatar" style="left:-50px;top:59px" role="img" aria-label="Customer portrait"></div>
    <div class="abs review-text" style="left:95px;top:28px">Sed ut perspiciatis unde omnis iste natus error sit voluptatem accusantium oremque laudantium, totam rem aperiam, eaque ipsa quae ab illo inventore veritatis et quasi architecto beatae vitae dicta sunt explicabo. Nemo enim ipsam voluptatem</div>
    <div class="abs reviewer" style="left:95px;top:184px">John Doe - &nbsp;Vantolia</div>
    <div class="abs stars" style="left:95px;top:214px">★★★★★</div>
    <div class="abs quote" style="left:298px;top:170px">”</div>
  </div>
</section>

<section class="demo">
  <div class="demo-bg" role="img" aria-label="Orange tinted photo of a desk with coffee cup and keyboard"></div>
  <h2 class="abs">REQUEST A FREE DEMO</h2>
  <div class="abs field" style="left:251px;top:165px;width:336px;height:38px">Name</div>
  <div class="abs field" style="left:608px;top:165px;width:336px;height:38px">Phone</div>
  <div class="abs field" style="left:251px;top:225px;width:336px;height:38px">Email</div>
  <div class="abs field" style="left:608px;top:225px;width:336px;height:38px">Subject</div>
  <div class="abs field" style="left:251px;top:282px;width:693px;height:38px">Address</div>
  <div class="abs field" style="left:251px;top:338px;width:693px;height:72px">Message</div>
  <div class="abs submit">SUBMIT</div>
</section>

<footer class="site-footer">
  <div class="abs footer-links">Home &nbsp;| &nbsp;About Us &nbsp;| &nbsp;Our Services &nbsp;| &nbsp;Contact Us &nbsp;| &nbsp;Team</div>
  <div class="abs copyright">Vantolia © 2019 All Rights Reserved | Privacy Policy</div>
  <div class="abs social" style="left:534px" role="img" aria-label="Social profile link"></div>
  <div class="abs social" style="left:582px" role="img" aria-label="Social profile link"></div>
  <div class="abs social" style="left:630px" role="img" aria-label="Video channel link"></div>
</footer>

</body>
</html>
```